Professional Stationery Design - 16062020

Professional Logo, BCard, Email Signature & Letterhead design. This is the stationary design project for a professional Management Services Company

Target Market(s)

All

Industry/Entity Type

Management Solution

Requirements
Must have
• Professional

```html
<!DOCTYPE html>
<html lang="en">
<head>
<meta charset="utf-8">
<title>Corvana Management Services – Letterhead</title>
<link rel="stylesheet" href="https://fonts.googleapis.com/css2?family=Open+Sans:wght@400;600&family=Roboto:wght@400;500&display=swap">
<style>
  :root {
    --backdrop: #dcdcdc;
    --paper: #f9f9f9;
    --navy: #2f3a5a;
    --body-text: #5c5c5c;
    --footer-text: #4a4a4a;
    --signature-ink: #d9d9db;
  }
  * { box-sizing: border-box; margin: 0; padding: 0; }
  html, body {
    width: 1200px; height: 800px; overflow: hidden;
    background: var(--backdrop);
  }
  .sheet-row { position: relative; width: 1200px; height: 800px; }
  .letterhead {
    position: absolute; top: 111px;
    width: 412px; height: 574px;
    background: var(--paper);
    font-family: "Open Sans", sans-serif;
    color: var(--body-text);
  }
  .letterhead--first { left: 165px; }
  .letterhead--second { left: 613px; }

  .brand {
    position: absolute; top: 50px; left: 0; right: 0;
    text-align: center;
    font-family: "Open Sans", sans-serif;
    font-weight: 600;
    color: var(--navy);
    line-height: 1.1;
  }
  .brand__name { display: block; font-size: 21px; letter-spacing: 2px; }
  .brand__sub { display: block; font-size: 8px; letter-spacing: 1px; margin-top: 3px; }

  .letter {
    position: absolute; top: 127px; left: 37px; width: 334px;
    font-size: 7.6px; line-height: 11.1px;
  }
  .letter p { margin-bottom: 11px; text-align: justify; }
  .letter .greeting, .letter .sign-off { text-align: left; }
  .signature {
    display: block; width: 48px; height: 44px; margin-top: 4px;
    background: var(--signature-ink);
  }

  .contact {
    position: absolute; top: 508px; left: 37px; right: 42px;
    display: flex; justify-content: space-between;
    font-family: "Roboto", sans-serif;
    font-size: 8.2px; line-height: 10.7px;
    color: var(--footer-text);
  }
  .contact__line { display: flex; align-items: center; gap: 3px; }
  .contact__icon { width: 8px; height: 8px; fill: var(--navy); }
  .office { text-align: right; }
  .office__title { color: var(--navy); font-weight: 500; }
</style>
</head>
<body>
<main class="sheet-row">

  <article class="letterhead letterhead--first">
    <header class="brand">
      <span class="brand__name">CORVANA</span>
      <span class="brand__sub">MANAGEMENT SERVICES</span>
    </header>
    <section class="letter">
      <p class="greeting">Dear customer,</p>
      <p>Lorem ipsum dolor sit amet, consectetur adipisicing elit, sed do eiusmod tempor incididunt ut labore et dolore magna aliqua. Ut enim ad minim veniam, quis nostrud exercitation ullamco laboris nisi ut aliquip ex ea commodo consequat. Duis aute irure dolor in reprehenderit in voluptate velit esse cillum dolore eu fugiat nulla pariatur. Excepteur sint occaecat cupidatat non proident, sunt in culpa qui officia deserunt mollit anim id est laborum.</p>
      <p>Lorem ipsum dolor sit amet, consectetur adipisicing elit, sed do eiusmod tempor incididunt ut labore et dolore magna aliqua. Ut enim ad minim veniam, quis nostrud exercitation ullamco laboris nisi ut aliquip ex ea commodo consequat. Duis aute irure dolor in reprehenderit in voluptate velit esse cillum dolore eu fugiat nulla pariatur. Excepteur sint occaecat cupidatat non proident, sunt in culpa qui officia deserunt mollit anim id est laborum.</p>
      <p>Lorem ipsum dolor sit amet, consectetur adipisicing elit, sed do eiusmod tempor incididunt ut labore et dolore magna aliqua. Ut enim ad minim veniam, quis nostrud exercitation ullamco laboris nisi ut aliquip ex ea commodo consequat. Duis aute irure dolor in reprehenderit in voluptate velit esse cillum dolore eu fugiat nulla pariatur. Excepteur sint occaecat cupidatat non proident, sunt in culpa qui officia deserunt mollit anim id est laborum.</p>
      <p>Lorem ipsum dolor sit amet, consectetur adipisicing elit, sed do eiusmod tempor incididunt ut labore et dolore magna aliqua. Ut enim ad minim veniam, quis nostrud exercitation ullamco laboris nisi ut aliquip ex ea commodo consequat. Duis aute irure dolor in reprehenderit.</p>
      <p class="sign-off">Yours Sincerely,</p>
      <span class="signature" role="img" aria-label="Handwritten signature"></span>
    </section>
    <footer class="contact">
      <div class="contact__details">
        <div class="contact__line"><svg class="contact__icon" viewBox="0 0 10 10"><path d="M1 4c0-2 2-3 4-3s4 1 4 3H7V3H3v1zM2 5h6l1 4H1z"/></svg>(555) 014-2290</div>
        <div class="contact__line"><svg class="contact__icon" viewBox="0 0 10 10"><path d="M0 2h10v6H0z M0.8 2.6 5 5.6 9.2 2.6" stroke="#f9f9f9" stroke-width="0.8"/></svg>info@corvana-ms.com</div>
        <div class="contact__line"><svg class="contact__icon" viewBox="0 0 10 10"><circle cx="5" cy="5" r="4.5"/><path d="M2 5h6M5 1v8" stroke="#f9f9f9" stroke-width="0.8"/></svg>www.corvana-ms.com</div>
      </div>
      <address class="office" style="font-style:normal">
        <div class="office__title">Harbour Office</div>
        <div>218 Alder Street 400</div>
        <div>Westport, WA 98000</div>
      </address>
    </footer>
  </article>

  <article class="letterhead letterhead--second">
    <header class="brand">
      <span class="brand__name">CORVANA</span>
      <span class="brand__sub">MANAGEMENT SERVICES</span>
    </header>
    <section class="letter">
      <p class="greeting">Dear customer,</p>
      <p>Lorem ipsum dolor sit amet, consectetur adipisicing elit, sed do eiusmod tempor incididunt ut labore et dolore magna aliqua. Ut enim ad minim veniam, quis nostrud exercitation ullamco laboris nisi ut aliquip ex ea commodo consequat. Duis aute irure dolor in reprehenderit in voluptate velit esse cillum dolore eu fugiat nulla pariatur. Excepteur sint occaecat cupidatat non proident, sunt in culpa qui officia deserunt mollit anim id est laborum.</p>
      <p>Lorem ipsum dolor sit amet, consectetur adipisicing elit, sed do eiusmod tempor incididunt ut labore et dolore magna aliqua. Ut enim ad minim veniam, quis nostrud exercitation ullamco laboris nisi ut aliquip ex ea commodo consequat. Duis aute irure dolor in reprehenderit in voluptate velit esse cillum dolore eu fugiat nulla pariatur. Excepteur sint occaecat cupidatat non proident, sunt in culpa qui officia deserunt mollit anim id est laborum.</p>
      <p>Lorem ipsum dolor sit amet, consectetur adipisicing elit, sed do eiusmod tempor incididunt ut labore et dolore magna aliqua. Ut enim ad minim veniam, quis nostrud exercitation ullamco laboris nisi ut aliquip ex ea commodo consequat. Duis aute irure dolor in reprehenderit in voluptate velit esse cillum dolore eu fugiat nulla pariatur. Excepteur sint occaecat cupidatat non proident, sunt in culpa qui officia deserunt mollit anim id est laborum.</p>
      <p>Lorem ipsum dolor sit amet, consectetur adipisicing elit, sed do eiusmod tempor incididunt ut labore et dolore magna aliqua. Ut enim ad minim veniam, quis nostrud exercitation ullamco laboris nisi ut aliquip ex ea commodo consequat. Duis aute irure dolor in reprehenderit.</p>
      <p class="sign-off">Yours Sincerely,</p>
      <span class="signature" role="img" aria-label="Handwritten signature"></span>
    </section>
    <footer class="contact">
      <div class="contact__details">
        <div class="contact__line"><svg class="contact__icon" viewBox="0 0 10 10"><path d="M1 4c0-2 2-3 4-3s4 1 4 3H7V3H3v1zM2 5h6l1 4H1z"/></svg>(555) 014-2290</div>
        <div class="contact__line"><svg class="contact__icon" viewBox="0 0 10 10"><path d="M0 2h10v6H0z M0.8 2.6 5 5.6 9.2 2.6" stroke="#f9f9f9" stroke-width="0.8"/></svg>info@corvana-ms.com</div>
        <div class="contact__line"><svg class="contact__icon" viewBox="0 0 10 10"><circle cx="5" cy="5" r="4.5"/><path d="M2 5h6M5 1v8" stroke="#f9f9f9" stroke-width="0.8"/></svg>www.corvana-ms.com</div>
      </div>
      <address class="office" style="font-style:normal">
        <div class="office__title">Harbour Office</div>
        <div>218 Alder Street 400</div>
        <div>Westport, WA 98000</div>
      </address>
    </footer>
  </article>

</main>
</body>
</html>
```